winery and bed & breakfast business card

need a business card design
font and style same as our marketing material
also need something for letterhead

not too colorful, we want professional and simple
name
address
phone number
web site
email
Corvelli Vineyard believes raising a family, living and working passionately with wine on the East End is a privilege. They consider the greatest accolades received over the years have been the thousands of satisfied tasting room visitors. Enlightening visitors to their products and wine region are the most important reasons they continue to make wine on the North Fork
We have created a casual and cozy environment within a rustic historic barn.
An outside seating area nestled among the vines provides visitors with unforgettable sunset views as they enjoy Corvelli’s quality crafted wines.

Target Market(s)

adults over 21

Font styles to use
Serif

Colors
6b449b
ffc214
f78f20
ffffff

Requirements
Must have
• logo
• same font as attached
• logo colors

```html
<!DOCTYPE html>
<html lang="en">
<head>
<meta charset="utf-8">
<title>Corvelli Vineyard – Business Card &amp; Letterhead</title>
<link rel="stylesheet" href="https://fonts.googleapis.com/css2?family=Cinzel:wght@400;600&family=Raleway:wght@400;500&display=swap">
<style>
  :root {
    --orange: #f29223;
    --plum: #4b3157;
    --white: #ffffff;
    --ink: #4a4450;
    --grey: #8a8a8a;
    --paper-shadow: 0 1px 4px rgba(0,0,0,.35);
  }
  * { box-sizing: border-box; margin: 0; padding: 0; }
  html, body { width: 900px; height: 1200px; overflow: hidden; background: var(--white); }
  body { position: relative; font-family: "Raleway", Arial, sans-serif; }

  .sheet { position: absolute; box-shadow: var(--paper-shadow); overflow: hidden; }
  .sheet-art { position: absolute; inset: 0; width: 100%; height: 100%; }

  .card-front { left: 14px; top: 5px; width: 431px; height: 258px; background: var(--orange); }
  .card-back  { left: 460px; top: 5px; width: 431px; height: 258px; background: var(--white); }
  .letterhead { left: 102px; top: 285px; width: 702px; height: 904px; background: var(--white); }

  .brand { position: absolute; display: flex; flex-direction: column; align-items: center; transform: translateX(-50%); }
  .brand-dot { border-radius: 50%; background: var(--orange); }
  .brand-name {
    font-family: "Cinzel", "Times New Roman", serif; font-weight: 600;
    color: var(--plum); white-space: nowrap; letter-spacing: .12em;
  }
  .card-front .brand { left: 216px; top: 54px; }
  .card-front .brand-dot { width: 100px; height: 100px; background: var(--white); }
  .card-front .brand-name { font-size: 22px; margin-top: 26px; }

  .card-back .brand { left: 120px; top: 34px; }
  .card-back .brand-dot { width: 72px; height: 72px; }
  .card-back .brand-name { font-size: 15px; margin-top: 24px; }

  .letterhead .brand { left: 119px; top: 42px; }
  .letterhead .brand-dot { width: 76px; height: 76px; }
  .letterhead .brand-name { font-size: 17px; margin-top: 36px; }

  .holder { position: absolute; left: 227px; top: 62px; }
  .holder-name { font-family: "Cinzel", "Times New Roman", serif; font-size: 18px; color: var(--ink); letter-spacing: .02em; }
  .holder-role { font-size: 13px; color: var(--ink); margin-top: 3px; }

  .contact { position: absolute; list-style: none; }
  .contact li { display: flex; align-items: center; white-space: nowrap; }
  .contact .icon { flex: none; }

  .card-back .contact { top: 199px; font-size: 13px; color: #fff3e4; }
  .card-back .contact li { height: 21px; }
  .card-back .contact .icon { width: 13px; height: 13px; margin-right: 9px; fill: var(--plum); }
  .card-back .contact-left { left: 46px; }
  .card-back .contact-right { left: 256px; }

  .letterhead .contact { font-size: 14px; }
  .letterhead .contact li { height: 26px; }
  .letterhead .contact .icon { width: 20px; height: 20px; margin-right: 15px; }
  .letterhead .contact-left { left: 42px; top: 803px; color: var(--grey); }
  .letterhead .contact-left .icon { fill: var(--orange); }
  .letterhead .contact-right { left: 474px; top: 842px; color: var(--white); }
  .letterhead .contact-right .icon { fill: var(--plum); }
</style>
</head>
<body>

<svg width="0" height="0" style="position:absolute" aria-hidden="true">
  <symbol id="icon-home" viewBox="0 0 20 20"><path d="M10 2 1 10h3v8h5v-5h2v5h5v-8h3z"/></symbol>
  <symbol id="icon-phone" viewBox="0 0 20 20"><path d="M6 1h8a2 2 0 0 1 2 2v14a2 2 0 0 1-2 2H6a2 2 0 0 1-2-2V3a2 2 0 0 1 2-2zm0 3v8h8V4z"/></symbol>
  <symbol id="icon-globe" viewBox="0 0 20 20"><path d="M10 1a9 9 0 1 0 0 18 9 9 0 0 0 0-18zm-1 2.1V7H6.3c.6-2 1.6-3.5 2.7-3.9zm2 0c1.1.4 2.1 1.9 2.7 3.9H11zM4.6 7H3.7a7 7 0 0 1 2.6-3 10 10 0 0 0-1.7 3zm10.8 0a10 10 0 0 0-1.7-3 7 7 0 0 1 2.6 3zM3.1 9h1.3a14 14 0 0 0 0 2H3.1a7 7 0 0 1 0-2zm3.3 0H9v2H6.4a12 12 0 0 1 0-2zM11 9h2.6a12 12 0 0 1 0 2H11zm4.6 0h1.3a7 7 0 0 1 0 2h-1.3a14 14 0 0 0 0-2zM3.7 13h.9a10 10 0 0 0 1.7 3 7 7 0 0 1-2.6-3zm2.6 0H9v3.9c-1.1-.4-2.1-1.9-2.7-3.9zm4.7 0h2.7c-.6 2-1.6 3.5-2.7 3.9zm4.4 0h.9a7 7 0 0 1-2.6 3 10 10 0 0 0 1.7-3z"/></symbol>
  <symbol id="icon-mail" viewBox="0 0 20 20"><path d="M1 4h18v12H1zm2 2v.4l7 5 7-5V6zm0 2.8V14h14V8.8l-7 5z"/></symbol>
</svg>

<section class="sheet card-front" aria-label="Business card front">
  <div class="brand">
    <span class="brand-dot"></span>
    <span class="brand-name">CORVELLI VINEYARD</span>
  </div>
</section>

<section class="sheet card-back" aria-label="Business card back">
  <svg class="sheet-art" viewBox="0 0 464 280" preserveAspectRatio="none" aria-hidden="true">
    <path fill="var(--orange)" d="M0 197C150 214 300 168 464 178V280H0Z"/>
    <path fill="var(--plum)" d="M0 165C120 200 300 128 464 146V168C300 154 150 208 0 190Z"/>
  </svg>
  <div class="brand">
    <span class="brand-dot"></span>
    <span class="brand-name">CORVELLI VINEYARD</span>
  </div>
  <div class="holder">
    <p class="holder-name">NAME SURNAME</p>
    <p class="holder-role">Ocupation</p>
  </div>
  <ul class="contact contact-left">
    <li><svg class="icon"><use href="#icon-home"/></svg>address</li>
    <li><svg class="icon"><use href="#icon-phone"/></svg>phone number</li>
  </ul>
  <ul class="contact contact-right">
    <li><svg class="icon"><use href="#icon-globe"/></svg>web site</li>
    <li><svg class="icon"><use href="#icon-mail"/></svg>email</li>
  </ul>
</section>

<section class="sheet letterhead" aria-label="Letterhead">
  <svg class="sheet-art" viewBox="0 0 756 979" preserveAspectRatio="none" aria-hidden="true">
    <path fill="var(--orange)" d="M90 979C350 962 550 896 756 886V979Z"/>
    <path fill="var(--plum)" d="M0 930C200 992 450 878 756 854V874C450 904 250 992 0 976Z"/>
  </svg>
  <div class="brand">
    <span class="brand-dot"></span>
    <span class="brand-name">CORVELLI VINEYARD</span>
  </div>
  <ul class="contact contact-left">
    <li><svg class="icon"><use href="#icon-home"/></svg>address</li>
    <li><svg class="icon"><use href="#icon-phone"/></svg>phone number</li>
  </ul>
  <ul class="contact contact-right">
    <li><svg class="icon"><use href="#icon-globe"/></svg>www.web site.com</li>
    <li><svg class="icon"><use href="#icon-mail"/></svg>email</li>
  </ul>
</section>

</body>
</html>
```